Business Card Design

Bowen therapy is a gentle therapy where moves are made(using your hands) over muscles or joint areas create myofascial release enabling the body to rebalance itself.

Its relaxing and have heal a variety of aliments . n contrast to other hands-on modalities, where the practitioner imposes correction on the client through manipulation, Bowen Technique facilitates the body in healing itself, with minimal intervention. Because of the subtle nature of Bowen Technique, and the body's continuing response to it over several days thereafter, other forms of manipulative therapy are discouraged for up to five days after a session, as they may interfere with the efficacy of the work.

Its an energy healing work using hands.
Its relaxing but professional.
I'm think of using blues, no greens or yellows. Some wave lines .

Target Market(s)

Anybody-

Industry/Entity Type

Business

Contact Information for Business Card

Marnie's Kessel Therapy,Marnie Fletcher, Bowen Therapist,Cert IV Kinlark
Ashvale, Corran Cove, Bellmont, 0467 305918,Gentle therapy restoring body balance.

Requirements
Must have
• Back needs a appointment table
with this wording :
Bowen Therapy is a subtle gentle bodywork therapy where a series of moves are made over muscles that can be used to address a wide range of conditions. It is suitable for skeletal, joint and muscle problems as well as for babies and children
Date Time.

If you are unable to keep your appointment, please contact us as soon as possible.

0467305918 ozmarnie@fernmail.net
Should not have
• Dont like times new roman and handwritten script font.

```html
<!DOCTYPE html>
<html lang="en">
<head>
<meta charset="utf-8">
<title>Marnie's Kessel Therapy – Business Cards</title>
<link rel="stylesheet" href="https://fonts.googleapis.com/css2?family=Arimo:wght@400;700&family=Exo+2:wght@400;500;600&display=swap">
<style>
  :root {
    --backdrop: #e4e8ec;
    --card-white: #ffffff;
    --band-blue: #5b8fc7;
    --band-blue-deep: #3f74ad;
    --tag-navy: #1f3f66;
    --ink: #23364d;
    --ink-soft: #4a5d73;
    --tag-ink: #f2f6fb;
    --rule: #b9cde3;
    --wave: rgba(255,255,255,.45);
  }
  * { box-sizing: border-box; margin: 0; padding: 0; }
  html, body {
    width: 1200px; height: 898px; overflow: hidden;
    background: var(--backdrop);
  }
  .stage {
    position: relative; width: 1200px; height: 898px;
    display: flex; align-items: center; justify-content: center; gap: 40px;
  }
  .card {
    position: relative; width: 540px; height: 310px; overflow: hidden;
    background: var(--card-white);
    box-shadow: 0 6px 18px rgba(0,0,0,.16);
  }

  /* Back card with appointment table */
  .card-back .side-band {
    position: absolute; top: 0; bottom: 0; width: 68px;
  }
  .card-back .side-band.left { left: 0; }
  .card-back .side-band.right { right: 0; }
  .appointment {
    position: absolute; left: 88px; right: 88px; top: 16px; bottom: 14px;
    display: flex; flex-direction: column;
    font-family: "Exo 2", sans-serif; color: var(--ink);
  }
  .appointment .business-name {
    font: 400 19px/1.1 "Arimo", sans-serif; text-align: center; color: var(--ink);
    margin-bottom: 7px;
  }
  .appointment .about {
    font-size: 8.6px; line-height: 1.38; color: var(--ink-soft); text-align: center;
    margin-bottom: 8px;
  }
  .appointment-table {
    width: 100%; border-collapse: collapse; font-size: 9.5px;
  }
  .appointment-table th {
    background: var(--band-blue); color: var(--tag-ink);
    font-weight: 600; text-align: left; padding: 3px 8px; letter-spacing: .05em;
  }
  .appointment-table td {
    height: 19px; border-bottom: 1px solid var(--rule);
  }
  .appointment-table .col-date { width: 55%; }
  .appointment .notice {
    font-size: 8.6px; line-height: 1.3; text-align: center; color: var(--ink-soft);
    margin-top: 8px;
  }
  .appointment .back-contact {
    margin-top: auto; display: flex; justify-content: center; gap: 18px;
    font-size: 10px; font-weight: 500; color: var(--tag-navy);
  }

  /* Front card */
  .card-front .blue-panel { position: absolute; inset: 0; }
  .card-front .business-name {
    position: absolute; left: 30px; top: 52px; width: 260px;
    font: 400 33px/1.08 "Arimo", sans-serif; color: var(--ink); text-align: center;
  }
  .card-front .tagline {
    position: absolute; left: 30px; top: 132px; width: 260px;
    font: 400 10px/1.2 "Exo 2", sans-serif; color: var(--ink-soft);
    text-align: center; letter-spacing: .04em;
  }
  .card-front .name-tag {
    position: absolute; left: 300px; top: 118px; width: 240px; height: 28px;
    display: flex; align-items: center; gap: 7px; padding-left: 26px;
    font: 500 11px/1 "Exo 2", sans-serif; letter-spacing: .06em;
    color: var(--tag-ink); text-transform: uppercase;
  }
  .name-tag .divider { width: 1px; height: 13px; background: var(--tag-ink); }
  .name-tag .role { font-size: 9px; }
  .contact-block {
    position: absolute; left: 38px; top: 182px;
    font: 400 10px/1.35 "Exo 2", sans-serif; color: var(--ink); letter-spacing: .03em;
  }
  .contact-block .credential { font-weight: 600; margin-bottom: 7px; }
  .contact-list { list-style: none; }
  .contact-list li { display: flex; align-items: center; gap: 7px; height: 16px; }
  .contact-list svg { width: 9px; height: 9px; fill: var(--tag-navy); flex: none; }
</style>
</head>
<body>
<main class="stage">

  <section class="card card-back" aria-label="Card back">
    <svg class="side-band left" viewBox="0 0 68 310" preserveAspectRatio="none" aria-hidden="true">
      <rect width="68" height="310" fill="var(--band-blue)"/>
      <path d="M0 90 C20 70 45 110 68 88" stroke="var(--wave)" stroke-width="1.5" fill="none"/>
      <path d="M0 150 C20 130 45 170 68 148" stroke="var(--wave)" stroke-width="1.5" fill="none"/>
      <path d="M0 210 C20 190 45 230 68 208" stroke="var(--wave)" stroke-width="1.5" fill="none"/>
    </svg>
    <svg class="side-band right" viewBox="0 0 68 310" preserveAspectRatio="none" aria-hidden="true">
      <rect width="68" height="310" fill="var(--band-blue)"/>
      <path d="M0 90 C20 70 45 110 68 88" stroke="var(--wave)" stroke-width="1.5" fill="none"/>
      <path d="M0 150 C20 130 45 170 68 148" stroke="var(--wave)" stroke-width="1.5" fill="none"/>
      <path d="M0 210 C20 190 45 230 68 208" stroke="var(--wave)" stroke-width="1.5" fill="none"/>
    </svg>
    <div class="appointment">
      <h2 class="business-name">Marnie's Kessel Therapy</h2>
      <p class="about">Bowen Therapy is a subtle gentle bodywork therapy where a series of moves are made over muscles that can be used to address a wide range of conditions. It is suitable for skeletal, joint and muscle problems as well as for babies and children</p>
      <table class="appointment-table">
        <thead><tr><th class="col-date">Date</th><th>Time</th></tr></thead>
        <tbody>
          <tr><td></td><td></td></tr>
          <tr><td></td><td></td></tr>
          <tr><td></td><td></td></tr>
        </tbody>
      </table>
      <p class="notice">If you are unable to keep your appointment, please contact us as soon as possible.</p>
      <p class="back-contact"><span>0467305918</span><span>ozmarnie@fernmail.net</span></p>
    </div>
  </section>

  <section class="card card-front" aria-label="Card front">
    <svg class="blue-panel" viewBox="0 0 540 310" preserveAspectRatio="none" aria-hidden="true">
      <polygon points="300,0 540,0 540,310 330,310 330,150 300,118" fill="var(--band-blue)"/>
      <path d="M330 200 C380 175 430 225 480 198 S540 190 540 190" stroke="var(--wave)" stroke-width="1.5" fill="none"/>
      <path d="M330 230 C380 205 430 255 480 228 S540 220 540 220" stroke="var(--wave)" stroke-width="1.5" fill="none"/>
      <path d="M330 260 C380 235 430 285 480 258 S540 250 540 250" stroke="var(--wave)" stroke-width="1.5" fill="none"/>
      <path d="M310 40 C360 15 420 65 470 38 S540 30 540 30" stroke="var(--wave)" stroke-width="1.5" fill="none"/>
      <path d="M310 70 C360 45 420 95 470 68 S540 60 540 60" stroke="var(--wave)" stroke-width="1.5" fill="none"/>
      <polygon points="300,118 540,118 540,146 322,146" fill="var(--tag-navy)"/>
    </svg>
    <h1 class="business-name">Marnie's Kessel Therapy</h1>
    <p class="tagline">Gentle therapy restoring body balance.</p>
    <div class="name-tag">
      <span class="person">Marnie Fletcher</span>
      <span class="divider"></span>
      <span class="role">Bowen Therapist</span>
    </div>
    <div class="contact-block">
      <p class="credential">Cert IV Kinlark</p>
      <ul class="contact-list">
        <li><svg viewBox="0 0 10 10"><path d="M5 0 A3.5 3.5 0 0 1 8.5 3.5 C8.5 6 5 10 5 10 C5 10 1.5 6 1.5 3.5 A3.5 3.5 0 0 1 5 0 Z M5 2.2 A1.3 1.3 0 1 0 5.01 2.2 Z"/></svg>Ashvale, Corran Cove, Bellmont</li>
        <li><svg viewBox="0 0 10 10"><path d="M2 0.5 L3.6 2.5 L2.8 3.6 Q4 6 6.4 7.2 L7.5 6.4 L9.5 8 L8.3 9.5 Q3.5 9 0.5 1.7 Z"/></svg>0467 305918</li>
        <li><svg viewBox="0 0 10 10"><path d="M0 2 H10 V8.5 H0 Z M0.8 2.6 L5 5.6 L9.2 2.6 Z"/></svg>ozmarnie@fernmail.net</li>
      </ul>
    </div>
  </section>

</main>
</body>
</html>
```